LINGERIE WEBSHOP - Velora casa

We are looking for design and layout design for our webshop. We are company that sells lingerie and other connected textile products liki payamas and etc..
Our website will have approx 500 different products within 2 main catogories Woman/Man) and approx. 10 subcategories
Here is what we expect form design:
-Color pallete should be black and white (if you wish you can add some accent color)
-we want to leave feeling to customers of good quality products towards to luxury
-UX should be simple. Feel free to suggest layout
-frontpage layout, product list layout, product description layout, blog layout
-responsive design, compatible with smartphone

Target Market(s)

woman buying for themself, man buying for woman

Industry/Entity Type

Lingerie

Logo Text

VELORA CASA

Number of Pages Required

4 page

Font styles to use
Sans Serif
Decorative

Requirements
Must have
• simple UX
Nice to have
• difference for sexy/luxury lingerie and daily/cozy lingerie
Should not have
• cheap feel, unreliable

```html
<!DOCTYPE html>
<html lang="en">
<head>
<meta charset="utf-8">
<title>Velora casa — Lingerie</title>
<link href="https://fonts.googleapis.com/css2?family=Poppins:ital,wght@0,300;0,400;0,500;0,600;0,700;1,400&display=swap" rel="stylesheet">
<style>
:root{
  --ink:#151515;
  --navy:#1f1f22;
  --accent:#b0342b;
  --muted:#8a8a8a;
  --line:#e4e4e4;
  --soft:#f5f5f4;
  --white:#fff;
}
*{box-sizing:border-box;margin:0;padding:0}
html,body{width:1200px;height:3358px;overflow:hidden}
body{font-family:'Poppins',sans-serif;color:var(--ink);background:var(--white);position:relative}
a{color:inherit;text-decoration:none}
.wrap{width:878px;margin:0 auto;position:relative}
.topbar{height:35px;background:var(--navy);color:#fff;font-size:11px}
.topbar .wrap{display:flex;justify-content:space-between;align-items:center;height:35px}
.topbar .contact{display:flex;align-items:center;gap:6px}
.header{height:71px;border-bottom:1px solid var(--line)}
.header .wrap{display:flex;align-items:center;height:70px}
.brand{font-size:24px;font-weight:300;letter-spacing:1px;color:var(--ink);line-height:28px;width:160px;white-space:nowrap}
.search{margin-left:89px;display:flex;height:41px}
.search input{width:288px;border:1px solid #ccc;padding:0 16px;font-family:inherit;font-size:10px}
.search button{width:92px;background:var(--ink);color:#fff;border:0;font-family:inherit;font-size:11px}
.cart{margin-left:auto;display:flex;align-items:center;gap:6px;font-weight:600;font-size:14px}
.nav{height:41px;border-bottom:1px solid var(--line)}
.nav ul{list-style:none;display:flex;gap:35px;height:40px;align-items:center;font-size:12px}
.hero{height:433px;background:#ededed;position:relative;overflow:hidden}
.hero h1{position:absolute;left:161px;top:152px;font-size:32px;line-height:37px;font-weight:700;width:440px}
.hero h1 em{font-style:normal;color:var(--accent)}
.hero p{position:absolute;left:161px;top:240px;width:400px;font-size:12px;line-height:18px;color:#333}
.btn{display:inline-block;background:var(--ink);color:#fff;border-radius:20px;font-size:12px;font-weight:500}
.hero .btn{position:absolute;left:161px;top:292px;padding:10px 20px}
.hero-photo{position:absolute;left:605px;top:0;width:435px;height:433px;background:linear-gradient(90deg,#ececec 0,#c9a99a 12%,#b98f80 30%,#2b2b30 42%,#e3ded8 52%,#cfa38c 66%,#2a3150 80%,#ececec 100%)}
.dots{position:absolute;display:flex;gap:6px}
.dots i{width:9px;height:9px;border-radius:50%;background:#fff;border:1px solid #ccc;display:block}
.dots i.on{background:var(--ink);border-color:var(--ink)}
.promos{position:absolute;top:633px;left:161px;width:878px;height:168px;display:flex;gap:34px}
.promo{flex:1;position:relative;overflow:hidden}
.promo.summer{background:#f0f0f0}
.promo.upto{background:var(--navy);color:#fff}
.promo.new{background:#e9e6e2}
.ph{position:absolute}
.summer .ph{left:0;top:0;width:110px;height:168px;background:linear-gradient(90deg,#f0f0f0,#1a1a1a 20%,#2a2a2a 80%,#f0f0f0)}
.summer h3{position:absolute;left:130px;top:38px;width:130px;text-align:center;color:var(--ink);font-size:22px;line-height:27px;font-weight:600}
.summer .btn{position:absolute;left:134px;top:115px;padding:10px 20px}
.upto h3{position:absolute;left:38px;top:50px;font-size:31px;font-weight:500}
.upto span{position:absolute;left:43px;top:94px;font-size:14px;font-weight:500}
.upto .ph{right:20px;top:0;width:110px;height:168px;background:linear-gradient(var(--navy) 0,#8e2a2a 10%,#7a2424 42%,var(--navy) 52%,#0e0e0e 62%,#0e0e0e 88%,var(--navy))}
.new .ph{left:6px;top:20px;width:120px;height:148px;background:linear-gradient(#e9e6e2,#5a3b2c 30%,#c9a43c 55%,#b8922e)}
.new h4{position:absolute;right:50px;top:42px;font-size:19px;font-weight:400;letter-spacing:1px}
.new h3{position:absolute;right:10px;top:70px;color:var(--ink);font-size:23px;font-weight:600;letter-spacing:1px}
.new a{position:absolute;right:40px;top:107px;font-size:12px;text-decoration:underline;font-weight:500}
.sec-title{position:absolute;left:0;width:1200px;text-align:center;font-size:17px;font-weight:600}
.sec-title::after{content:"";display:block;width:60px;height:2px;background:var(--ink);margin:10px auto 0}
.arrows{position:absolute;left:983px;display:flex;gap:4px}
.arrows span{width:26px;height:26px;background:var(--navy);display:flex;align-items:center;justify-content:center}
.products{position:absolute;left:161px;width:878px;display:flex;gap:30px}
.card{width:197px;text-align:center}
.card .ph{position:relative;width:197px;height:253px;background:linear-gradient(90deg,#f3f1ef 0,#f3f1ef 25%,#d8bfae 40%,#cfb3a0 60%,#f3f1ef 75%)}
.card.dark .ph{background:linear-gradient(90deg,#efece9 0,#efece9 25%,#b8b4b0 40%,#a9a5a1 60%,#efece9 75%)}
.card h5{font-size:12px;font-weight:400;margin-top:13px}
.card.active h5{color:var(--accent)}
.price{font-size:12px;margin-top:6px}
.price s{color:var(--muted);margin-right:8px}
.price b{color:var(--accent);font-weight:400}
.card .add{position:absolute;left:42px;top:112px;padding:9px 21px;font-size:12px}
.card .acts{position:absolute;left:44px;top:210px;display:flex;gap:8px}
.card .acts i{width:30px;height:30px;border-radius:50%;background:var(--navy);display:flex;align-items:center;justify-content:center}
.discount{position:absolute;top:1273px;left:161px;width:878px;height:192px;display:flex}
.disc{flex:1;background:linear-gradient(90deg,#d9c7a6 0,#d6c29e 45%,#b89a78 60%,#2f6a62 80%,#b8a88c);position:relative;color:#fff;text-align:center}
.disc .txt{position:absolute;left:20px;top:28px;width:180px}
.disc .s{font-size:20px;font-weight:300;letter-spacing:1px;line-height:26px}
.disc .d{font-size:28px;font-weight:700;letter-spacing:2px;line-height:40px}
.disc .p{color:var(--ink);font-size:28px;font-weight:600;line-height:38px}
.disc .f{font-size:18px;font-weight:600;letter-spacing:1px;line-height:28px}
.testi{position:absolute;top:1935px;left:161px;width:878px;height:268px;background:var(--navy);color:#fff}
.testi .avatar{position:absolute;left:75px;top:54px;width:124px;height:124px;border-radius:50%;background:linear-gradient(#c9a070,#e0c2a4 60%,#f0e6dc);border:4px solid #fff}
.testi .q{position:absolute;left:224px;top:52px;font-size:30px;font-weight:700;line-height:20px}
.testi p{position:absolute;left:224px;top:82px;width:530px;font-size:11.5px;line-height:20px;font-weight:500}
.testi .who{position:absolute;left:224px;top:155px;font-size:12px;font-style:italic}
.testi .dots{left:418px;top:214px}
.testi .dots i{background:transparent;border-color:#fff}
.testi .dots i.on{background:#fff}
.news{position:absolute;top:2326px;left:161px;width:878px;display:flex;gap:33px}
.post{flex:1;height:303px;border:1px solid var(--line);text-align:center}
.post .ph{position:relative;height:160px;background:linear-gradient(90deg,#8a7a4a,#6a5a3a 30%,#2a2a3a 42%,#7a5a7a 52%,#2a2a3a 62%,#6a6a50 80%,#3a3a30)}
.post h5{font-size:12px;font-weight:600;margin-top:17px}
.post .meta{font-size:12px;color:var(--muted);margin-top:7px}
.post .meta b{color:var(--accent);font-weight:400}
.post p{font-size:11.5px;color:var(--muted);line-height:18px;margin:10px 30px 0}
.post a{display:block;color:var(--ink);font-size:11.5px;margin-top:12px;text-decoration:underline}
.follow{position:absolute;top:2672px;left:0;width:1200px;height:234px;background:var(--navy);color:#fff;text-align:center}
.follow h3{padding-top:54px;font-size:17px;font-weight:600}
.follow h3::after{content:"";display:block;width:60px;height:2px;background:#fff;margin:9px auto 0}
.follow p{font-size:12px;margin-top:20px}
.follow form{display:flex;justify-content:center;gap:12px;margin-top:20px}
.follow input{width:293px;height:37px;border-radius:20px;border:0;padding:0 18px;font-family:inherit;font-size:10px}
.follow button{width:126px;height:37px;border-radius:20px;border:1px solid #fff;background:transparent;color:#fff;font-family:inherit;font-size:12px}
.features{position:absolute;top:2906px;left:161px;width:878px;height:150px;display:flex;align-items:center}
.feat{width:227px;display:flex;align-items:center;gap:10px;border-right:1px solid #ccc;height:40px}
.feat:last-child{border:0}
.feat b{display:block;font-size:14px;font-weight:500;line-height:16px}
.feat small{font-size:8px;color:#555}
.footer{position:absolute;top:3056px;left:0;width:1200px;height:248px;background:var(--soft)}
.col{position:absolute;top:44px}
.col h6{font-size:13px;font-weight:500;margin-bottom:13px}
.col li{list-style:none;font-size:11.5px;color:var(--muted);line-height:21px}
.col p{font-size:11.5px;color:var(--muted);line-height:21px;width:258px}
.col .ci{display:flex;gap:8px;align-items:flex-start;font-size:11.5px;color:var(--muted);line-height:18px;margin-bottom:10px;width:272px}
.col .ci i{flex:none;width:20px;height:20px;border:1px solid var(--ink);border-radius:50%;display:flex;align-items:center;justify-content:center}
.bottom{position:absolute;top:3304px;left:0;width:1200px;height:54px;background:var(--navy);color:#fff;font-size:11px}
.bottom .wrap{display:flex;justify-content:space-between;align-items:center;height:54px}
.social{display:flex;gap:15px}
.social i{width:12px;height:12px;border-radius:50%;background:#fff;display:block}
</style>
</head>
<body>

<div class="topbar"><div class="wrap">
  <div class="contact">
    <svg width="13" height="13" viewBox="0 0 24 24"><path fill="#fff" d="M6.6 10.8a15 15 0 006.6 6.6l2.2-2.2c.3-.3.7-.4 1-.2 1.1.4 2.3.6 3.6.6.6 0 1 .4 1 1V20c0 .6-.4 1-1 1A17 17 0 013 4c0-.6.4-1 1-1h3.5c.6 0 1 .4 1 1 0 1.3.2 2.5.6 3.6.1.3 0 .7-.2 1z"/></svg>
    <span>+1 123-456-7890 |</span>
    <svg width="14" height="12" viewBox="0 0 24 20"><rect x="1" y="1" width="22" height="18" fill="none" stroke="#fff" stroke-width="2"/><path d="M1 2l11 9 11-9" fill="none" stroke="#fff" stroke-width="2"/></svg>
    <span>info@example.com</span>
  </div>
  <div>Login &nbsp;|&nbsp; Wishlist &nbsp;|&nbsp; My Account</div>
</div></div>

<header class="header"><div class="wrap">
  <a class="brand" href="#">VELORA CASA</a>
  <form class="search"><input placeholder="Search Product..."><button type="button">Search</button></form>
  <div class="cart">
    <svg width="30" height="26" viewBox="0 0 30 26"><path d="M1 2h5l4 14h14l3-10H8" fill="none" stroke="#333" stroke-width="1.8"/><circle cx="12" cy="22" r="2" fill="#333"/><circle cx="22" cy="22" r="2" fill="#333"/><circle cx="23" cy="5" r="5" fill="#b0342b"/></svg>
    $599 <svg width="8" height="6" viewBox="0 0 8 6"><path d="M1 1l3 3 3-3" fill="none" stroke="#111" stroke-width="1.6"/></svg>
  </div>
</div></header>

<nav class="nav"><div class="wrap"><ul>
  <li>Home</li><li>About Us</li><li>Products ▾</li><li>Shop ▾</li><li>Blog</li><li>Contact</li>
</ul></div></nav>

<section class="hero">
  <h1>Winter Collection Limited<br>Offer <em>20%</em> Off</h1>
  <p>Proin sagittis metus massa, at fringilla erat pellentesque non. Aliquam erat volutpat. Morbi fringilla ex eu ex ullamcorper</p>
  <a class="btn" href="#">Shop Now</a>
  <div class="hero-photo" role="img" aria-label="Two models wearing lace lingerie sets"></div>
  <div class="dots" style="left:580px;top:410px"><i></i><i class="on"></i><i></i></div>
</section>

<div class="promos">
  <div class="promo summer"><div class="ph" role="img" aria-label="Black lace camisole"></div><h3>Summer Fashion</h3><a class="btn" href="#">Shop Now</a></div>
  <div class="promo upto"><h3>Upto</h3><span>25% OFF</span><div class="ph" role="img" aria-label="Red lace bra and black brief"></div></div>
  <div class="promo new"><div class="ph" role="img" aria-label="Model in yellow hoodie"></div><h4>NEW</h4><h3>ARRIVALS</h3><a href="#">Shop Now</a></div>
</div>

<h2 class="sec-title" style="top:853px">POPULAR PRODUCTS</h2>
<div class="arrows" style="top:859px"><span><svg width="8" height="12"><path d="M6 1L1 6l5 5" stroke="#fff" stroke-width="2" fill="none"/></svg></span><span><svg width="8" height="12"><path d="M2 1l5 5-5 5" stroke="#fff" stroke-width="2" fill="none"/></svg></span></div>
<div class="products" style="top:917px">
  <div class="card"><div class="ph" role="img" aria-label="Model in white top and grey brief"></div><h5>Variable product 001</h5><div class="price"><s>$700</s><b>$500</b></div></div>
  <div class="card"><div class="ph" role="img" aria-label="Model in cream top and magenta brief"></div><h5>Variable product 001</h5><div class="price"><s>$700</s><b>$500</b></div></div>
  <div class="card dark active"><div class="ph" role="img" aria-label="Model in grey lace bodysuit">
    <a class="btn add" href="#">Add To Cart</a>
    <div class="acts"><i><svg width="14" height="12" viewBox="0 0 24 22"><path fill="#fff" d="M12 21l-9-9a5.5 5.5 0 019-7 5.5 5.5 0 019 7z"/></svg></i><i><svg width="14" height="10" viewBox="0 0 24 16"><path fill="#fff" d="M12 0C6 0 1 8 1 8s5 8 11 8 11-8 11-8S18 0 12 0z"/><circle cx="12" cy="8" r="3" fill="#1f1f22"/></svg></i><i><svg width="13" height="13" viewBox="0 0 24 24"><path d="M4 12a8 8 0 0114-5M20 12a8 8 0 01-14 5" stroke="#fff" stroke-width="3" fill="none"/><path fill="#fff" d="M19 2v7h-7zM5 22v-7h7z"/></svg></i></div>
  </div><h5>Variable product 001</h5><div class="price"><s>$700</s><b>$500</b></div></div>
  <div class="card"><div class="ph" role="img" aria-label="Model in navy lace lingerie set"></div><h5>Variable product 001</h5><div class="price"><s>$700</s><b>$500</b></div></div>
</div>

<div class="discount">
  <div class="disc" role="img" aria-label="Model in round sunglasses against a warm wall"><div class="txt"><div class="s">Super</div><div class="d">DISCOUNT</div><div class="p">35%</div><div class="f">Fashion</div></div></div>
  <div class="disc" role="img" aria-label="Model in round sunglasses against a warm wall"><div class="txt"><div class="s">Super</div><div class="d">DISCOUNT</div><div class="p">35%</div><div class="f">Fashion</div></div></div>
</div>

<h2 class="sec-title" style="top:1523px">BEST SELLER</h2>
<div class="arrows" style="top:1529px"><span><svg width="8" height="12"><path d="M6 1L1 6l5 5" stroke="#fff" stroke-width="2" fill="none"/></svg></span><span><svg width="8" height="12"><path d="M2 1l5 5-5 5" stroke="#fff" stroke-width="2" fill="none"/></svg></span></div>
<div class="products" style="top:1587px">
  <div class="card"><div class="ph" role="img" aria-label="Model in white top and grey brief"></div><h5>Variable product 001</h5><div class="price"><s>$700</s><b>$500</b></div></div>
  <div class="card"><div class="ph" role="img" aria-label="Model in cream top and magenta brief"></div><h5>Variable product 001</h5><div class="price"><s>$700</s><b>$500</b></div></div>
  <div class="card dark active"><div class="ph" role="img" aria-label="Model in grey lace bodysuit">
    <a class="btn add" href="#">Add To Cart</a>
    <div class="acts"><i><svg width="14" height="12" viewBox="0 0 24 22"><path fill="#fff" d="M12 21l-9-9a5.5 5.5 0 019-7 5.5 5.5 0 019 7z"/></svg></i><i><svg width="14" height="10" viewBox="0 0 24 16"><path fill="#fff" d="M12 0C6 0 1 8 1 8s5 8 11 8 11-8 11-8S18 0 12 0z"/><circle cx="12" cy="8" r="3" fill="#1f1f22"/></svg></i><i><svg width="13" height="13" viewBox="0 0 24 24"><path d="M4 12a8 8 0 0114-5M20 12a8 8 0 01-14 5" stroke="#fff" stroke-width="3" fill="none"/><path fill="#fff" d="M19 2v7h-7zM5 22v-7h7z"/></svg></i></div>
  </div><h5>Variable product 001</h5><div class="price"><s>$700</s><b>$500</b></div></div>
  <div class="card"><div class="ph" role="img" aria-label="Model in navy lace lingerie set"></div><h5>Variable product 001</h5><div class="price"><s>$700</s><b>$500</b></div></div>
</div>

<section class="testi">
  <div class="avatar" role="img" aria-label="Customer portrait"></div>
  <div class="q">“</div>
  <p>Maecenas semper aliquam massa. Praesent pharetra semvitae nisi eleifend mo-lestie.Aliquam molestie scelerisque ultricies. Suspendisse potenti. Lorem ipsum dolor sit amet, consectetur adipiscing elit. Vivamus tempor dictum ornare.</p>
  <div class="who">-John Doe</div>
  <div class="dots"><i></i><i class="on"></i><i></i></div>
</section>

<h2 class="sec-title" style="top:2260px">LATEST NEWS</h2>
<div class="news">
  <article class="post"><div class="ph" role="img" aria-label="Woman in hat against graffiti wall"></div><h5>SIMPLY TIPS FOR BEAUTY</h5><div class="meta">Posted by &nbsp;<b>admin - 6 Comments</b></div><p>Mauris eu euismod tellus curabi-tur a neque in nulla iaculis...</p><a href="#">READ MORE</a></article>
  <article class="post"><div class="ph" role="img" aria-label="Woman in hat against graffiti wall"></div><h5>SIMPLY TIPS FOR BEAUTY</h5><div class="meta">Posted by &nbsp;<b>admin - 6 Comments</b></div><p>Mauris eu euismod tellus curabi-tur a neque in nulla iaculis...</p><a href="#">READ MORE</a></article>
  <article class="post"><div class="ph" role="img" aria-label="Woman in hat against graffiti wall"></div><h5>SIMPLY TIPS FOR BEAUTY</h5><div class="meta">Posted by &nbsp;<b>admin - 6 Comments</b></div><p>Mauris eu euismod tellus curabi-tur a neque in nulla iaculis...</p><a href="#">READ MORE</a></article>
</div>

<section class="follow">
  <h3>FOLLOW OUR UPDATES!</h3>
  <p>If you want to get an email from us every time we have a new special offer, then sign up here!</p>
  <form><input placeholder="Enter Your Email"><button type="button">Subscribe</button></form>
</section>

<div class="features">
  <div class="feat"><svg width="38" height="26" viewBox="0 0 38 26"><rect x="0" y="2" width="24" height="17" fill="#1f1f22"/><path d="M24 7h8l5 6v6H24z" fill="#1f1f22"/><circle cx="8" cy="21" r="4" fill="#1f1f22" stroke="#fff" stroke-width="2"/><circle cx="29" cy="21" r="4" fill="#1f1f22" stroke="#fff" stroke-width="2"/></svg><div><b>FREE DELIVERY</b><small>WORLDWIDE</small></div></div>
  <div class="feat" style="padding-left:52px"><svg width="30" height="28" viewBox="0 0 30 28"><path d="M4 18v-4a11 11 0 0122 0v4" fill="none" stroke="#1f1f22" stroke-width="3"/><rect x="2" y="16" width="7" height="11" rx="2" fill="#1f1f22"/><rect x="21" y="16" width="7" height="11" rx="2" fill="#1f1f22"/></svg><div><b>24/ 7 SUPPORT</b><small>CUSTOMER SUPPORT</small></div></div>
  <div class="feat" style="padding-left:52px"><svg width="32" height="26" viewBox="0 0 32 26"><rect x="1" y="1" width="30" height="24" rx="3" fill="#1f1f22"/><rect x="5" y="7" width="22" height="12" rx="1" fill="#fff"/></svg><div><b>PAYMENT</b><small>SECURE SYSTEM</small></div></div>
  <div class="feat" style="padding-left:52px"><svg width="32" height="30" viewBox="0 0 32 30"><path d="M8 2h16v8a8 8 0 01-16 0z" fill="#1f1f22"/><path d="M8 5H2c0 6 3 8 6 8M24 5h6c0 6-3 8-6 8" fill="none" stroke="#1f1f22" stroke-width="2.5"/><rect x="14" y="17" width="4" height="6" fill="#1f1f22"/><rect x="9" y="23" width="14" height="5" fill="#1f1f22"/></svg><div><b>TRUSTED</b><small>ENUINE PRODUCTS</small></div></div>
</div>

<footer class="footer">
  <div class="col" style="left:161px"><h6>ABOUT US</h6><p>There are many variations of passages of Lorem Ipsum available, but the majority have suffered alteration in some form, by injected humour, or randomised words which don't look even slightly believable.</p></div>
  <div class="col" style="left:464px"><h6>CATEGORIES</h6><ul><li>Category 01</li><li>Category 02</li><li>Category 03</li><li>Category 04</li><li>Category 05</li><li>Category 06</li></ul></div>
  <div class="col" style="left:615px"><h6>MY ACCOUNT</h6><ul><li>Orders</li><li>Compare</li><li>Wishlist</li><li>Log In</li><li>Register</li></ul></div>
  <div class="col" style="left:767px"><h6>CONTACT INFO</h6>
    <div class="ci"><i><svg width="8" height="10" viewBox="0 0 8 10"><path d="M4 0a4 4 0 00-4 4c0 3 4 6 4 6s4-3 4-6a4 4 0 00-4-4z" fill="#151515"/></svg></i><span>Lorem ipsum is dolor amet lipsum is dolor amet lipsum is dolor amet</span></div>
    <div class="ci"><i><svg width="9" height="9" viewBox="0 0 24 24"><path fill="#151515" d="M6.6 10.8a15 15 0 006.6 6.6l2.2-2.2c.3-.3.7-.4 1-.2 1.1.4 2.3.6 3.6.6.6 0 1 .4 1 1V20c0 .6-.4 1-1 1A17 17 0 013 4c0-.6.4-1 1-1h3.5c.6 0 1 .4 1 1 0 1.3.2 2.5.6 3.6.1.3 0 .7-.2 1z"/></svg></i><span>(+1) 123-456-7890</span></div>
    <div class="ci"><i style="background:var(--ink)"><svg width="9" height="7" viewBox="0 0 24 20"><rect x="1" y="1" width="22" height="18" fill="none" stroke="#fff" stroke-width="3"/></svg></i><span>info@example.com</span></div>
  </div>
</footer>

<div class="bottom"><div class="wrap">
  <span>Copyright © 2020. All Rights Reserved.</span>
  <div class="social"><i></i><i></i><i></i><i></i><i></i></div>
</div></div>

</body>
</html>
```